Kelvor Datawise Solutions

We need a Logo and Website for our company based in London. We are a IT recruitment company . We provide quality resources to top IT company across UK.

Industry/Entity Type

It Company

Number of Pages Required

4 page

```html
<!DOCTYPE html>
<html lang="en">
<head>
<meta charset="utf-8">
<title>Kelvor Datawise Solutions</title>
<link rel="stylesheet" href="https://fonts.googleapis.com/css2?family=Fira+Sans:wght@400;600;700&family=Open+Sans:wght@300;400;600;700&display=swap">
<style>
:root{
  --page:#e6e6e6;
  --brand:#2f6fb3;
  --brand-light:#3b9bd8;
  --ink:#555;
  --ink-soft:#777;
  --white:#fff;
  --footer-top:#4a4a4a;
  --footer-bottom:#2a2a2a;
  --footer-text:#d6d6d6;
  --rule:#777;
}
*{margin:0;padding:0;box-sizing:border-box}
html,body{width:714px;height:1200px;overflow:hidden;background:var(--page)}
body{position:relative;font-family:"Open Sans",Arial,sans-serif;color:var(--ink)}
.site{position:absolute;left:9px;top:9px;width:697px;height:1183px;overflow:hidden}
.abs{position:absolute}

/* hero */
.hero{left:0;top:0;width:697px;height:327px;background:linear-gradient(100deg,#6b6e70 0%,#8c8f91 35%,#5d5f61 62%,#3c3d3f 80%,#262728 100%)}
.hero-logo{left:0;top:112px;width:697px;display:flex;justify-content:center;align-items:center;gap:8px}
.logo-mark{width:12px;height:12px;background:var(--brand-light)}
.logo-name{font-family:"Fira Sans",Arial,sans-serif;font-weight:400;font-size:18px;color:var(--white)}
.tagline{left:149px;top:203px;width:400px;height:59px;border:1px solid rgba(255,255,255,.85);display:flex;align-items:center;justify-content:center;text-align:center;font-family:"Fira Sans",Arial,sans-serif;font-weight:600;font-size:17.5px;line-height:24px;color:var(--white);letter-spacing:.2px}

/* welcome */
.welcome{left:0;top:327px;width:697px;height:256px;background:linear-gradient(#fff 0%,#fff 85%,#eeeeee 100%)}
.welcome-kicker{left:53px;top:34px;font-family:"Fira Sans",Arial,sans-serif;font-size:14px;color:#555}
.welcome-title{left:53px;top:51px;font-family:"Fira Sans",Arial,sans-serif;font-weight:600;font-size:17px;color:var(--brand)}
.welcome-rule{left:53px;top:72px;width:590px;height:1px;background:#ccc}
.welcome-rule::before{content:"";position:absolute;left:0;top:-1px;width:272px;height:2px;background:#666}
.welcome-text{left:53px;top:87px;width:592px;font-size:8.3px;line-height:12.9px;color:var(--ink-soft)}
.btn-more{left:53px;top:202px;width:89px;height:24px;background:var(--brand);color:var(--white);font-size:8px;font-weight:600;display:flex;align-items:center;justify-content:center;letter-spacing:.3px}

/* feature tiles */
.tile{height:208px;top:583px;color:var(--white);text-align:center}
.tile-services{left:0;width:349px;background:linear-gradient(160deg,#2d4a5e 0%,#5a7384 45%,#33495a 75%,#1b2a36 100%)}
.tile-careers{left:349px;width:348px;background:linear-gradient(160deg,#2c2d2f 0%,#6a6c6e 50%,#8a8b8c 70%,#3c3d3e 100%)}
.tile-title{position:absolute;left:0;right:0;top:84px;font-family:"Fira Sans",Arial,sans-serif;font-weight:600;font-size:16px}
.tile-sub{position:absolute;left:40px;right:40px;top:109px;font-size:11px;line-height:15px}

/* forms */
.panel{top:795px;height:190px;color:var(--white)}
.panel-contact{left:0;width:349px;background:linear-gradient(120deg,#3a2c22 0%,#5e4432 40%,#2a211b 70%,#15110e 100%)}
.panel-resume{left:349px;width:348px;background:linear-gradient(160deg,#2d2e30 0%,#3b3c3e 50%,#252628 100%)}
.panel-title{position:absolute;font-family:"Fira Sans",Arial,sans-serif;font-weight:700;font-size:14px;text-align:center}
.field{position:absolute;background:rgba(60,60,60,.55);border:1px solid rgba(255,255,255,.35);border-radius:2px;font-size:7.5px;font-weight:600;padding:2px 10px;color:var(--white)}
.btn-line{position:absolute;border:1px solid var(--white);border-radius:1px;font-size:7.5px;font-weight:600;display:flex;align-items:center;justify-content:center;color:var(--white);background:rgba(0,0,0,.4)}

/* footer */
.footer{left:0;top:985px;width:697px;height:198px;background:linear-gradient(var(--footer-top),var(--footer-bottom));color:var(--footer-text);font-family:"Open Sans",Arial,sans-serif}
.foot-head{position:absolute;top:24px;font-family:"Fira Sans",Arial,sans-serif;font-size:12px;color:#ddd}
.foot-head::after{content:"";position:absolute;left:0;top:21px;width:120px;height:1px;background:#666}
.foot-sep{position:absolute;top:48px;width:1px;height:95px;background:#5e5e5e}
.quick-links{position:absolute;left:40px;top:61px;list-style:none;font-size:9px;font-weight:300;line-height:15.7px}
.quick-links li::before{content:"›";margin-right:6px;font-weight:600}
.contact-list{position:absolute;left:173px;top:60px;font-size:9px;font-weight:300;line-height:12.5px}
.contact-row{position:relative;padding-left:15px;margin-bottom:12px}
.contact-row svg{position:absolute;left:0;top:1px}
.social-list{position:absolute;left:388px;top:61px;list-style:none;font-size:9px;font-weight:300;line-height:18px}
.social-list li{display:flex;align-items:center;gap:8px}
.social-dot{width:9px;height:9px;border-radius:50%;background:#ddd}
.foot-logo{position:absolute;left:510px;top:91px;display:flex;align-items:center;gap:6px}
.foot-logo .logo-name{font-size:12.5px}
.foot-rule{position:absolute;left:40px;top:181px;width:617px;height:1px;background:#555}
.copyright{position:absolute;left:0;right:0;top:186px;text-align:center;font-size:6px;color:#aaa;letter-spacing:.2px}
</style>
</head>
<body>
<main class="site">

  <section class="abs hero" role="img" aria-label="Photo of a businessman holding a briefcase against a cloudy city skyline">
    <div class="abs hero-logo"><span class="logo-mark"></span><span class="logo-name">Kelvor Datawise Solutions</span></div>
    <h1 class="abs tagline">SUPPORT PROFESSIONAL RELATIONSHIPS<br>WITH EACH OF OUR CUSTOMERS</h1>
  </section>

  <section class="abs welcome">
    <p class="abs welcome-kicker">WELCOME TO</p>
    <h2 class="abs welcome-title">Work KELVOR DATAWISE SOLUTIONS</h2>
    <div class="abs welcome-rule"></div>
    <p class="abs welcome-text">Lorem ipsum dolor sit amet, consectetuer adipiscing elit, sed diam nonummy nibh euismod tincidunt ut laoreet dolore magna aliquam erat volutpat. Ut wisi enim ad minim veniam, quis nostrud exerci tation ullamcorper suscipit lobortis nisl ut aliquip ex ea commodo consequat. Duis autem vel eum iriure dolor in hendrerit in vulputate velit esse molestie consequat, vel illum dolore eu feugiat nulla facilisis at vero eros et accumsan et iusto odio dignissim qui blandit praesent luptatum zzril delenit augue duis dolore te feugait nulla facilisi. Nam liber tempor cum soluta nobis eleifend option congue nihil imperdi doming id quod mazim placerat facer possim assum. Typi non habent claritatem insitam; est usus legentis in iis qui facit eorum claritatem. Investigatines demonstraverunt lectores legere me lius quod ii legunt saepius. Claritas est etiam processus dynamicus, qui sequitur mutationem consuetudium lecrum. Mirum est notare quam littera gothica, quam nunc putamus parum claram, anteposuerit litterarum formas humanitatis per seacula quarta decima et quinta decima. Eodem modo typi, qui nunc nobis videntur parum clari, fiant sollemnes in futurum.</p>
    <a class="abs btn-more">READ MORE</a>
  </section>

  <section class="abs tile tile-services" role="img" aria-label="Photo of business people walking in a blurred crowd beneath a word cloud">
    <h3 class="tile-title">SERVICES</h3>
    <p class="tile-sub">Explore what we can do for you</p>
  </section>
  <section class="abs tile tile-careers" role="img" aria-label="Photo of a businessman with a briefcase beside a city waterfront">
    <h3 class="tile-title">CAREERS</h3>
    <p class="tile-sub">See how we can help you find the career you've always wanted</p>
  </section>

  <section class="abs panel panel-contact" role="img" aria-label="Photo of a highway at night with light trails">
    <h3 class="panel-title" style="left:100px;width:149px;top:26px">Contact Us Now!</h3>
    <div class="field" style="left:100px;top:56px;width:149px;height:15px">Name</div>
    <div class="field" style="left:100px;top:75px;width:149px;height:15px">Phone</div>
    <div class="field" style="left:100px;top:95px;width:149px;height:15px">Email</div>
    <div class="field" style="left:100px;top:113px;width:149px;height:42px">Message</div>
    <div class="btn-line" style="left:100px;top:158px;width:51px;height:18px">SEND</div>
  </section>
  <section class="abs panel panel-resume" role="img" aria-label="Photo of a businessman standing on a tall stack of books">
    <h3 class="panel-title" style="left:100px;width:168px;top:75px">Upload Your Resume</h3>
    <div class="field" style="left:108px;top:102px;width:149px;height:16px"></div>
    <div class="btn-line" style="left:108px;top:121px;width:45px;height:15px">BROWSE</div>
    <div class="btn-line" style="left:156px;top:121px;width:33px;height:15px">SEND</div>
  </section>

  <footer class="abs footer">
    <h4 class="foot-head" style="left:40px">Quick Links</h4>
    <ul class="quick-links">
      <li>Home</li><li>About Us</li><li>Our Services</li><li>Why Choose Us</li><li>Contact Us</li>
    </ul>
    <div class="foot-sep" style="left:143px"></div>

    <h4 class="foot-head" style="left:173px">Contact Detail</h4>
    <div class="contact-list">
      <div class="contact-row">
        <svg width="8" height="10" viewBox="0 0 8 10"><path d="M4 0a4 4 0 0 1 4 4c0 3-4 6-4 6S0 7 0 4a4 4 0 0 1 4-4z" fill="#ddd"/><circle cx="4" cy="4" r="1.5" fill="#444"/></svg>
        KELVOR DATAWISE SOLUTIONS<br>Lorem ipsum drive, Suite # 108<br>London
      </div>
      <div class="contact-row">
        <svg width="10" height="9" viewBox="0 0 10 9"><path d="M1 2c2-2 6-2 8 0v1.5H7V2.5H3v1H1z" fill="#ddd"/><rect x="2" y="4.5" width="6" height="4" rx="1" fill="#ddd"/></svg>
        +44 20 7946 0321
      </div>
      <div class="contact-row">
        <svg width="10" height="8" viewBox="0 0 10 8"><rect x="0.5" y="0.5" width="9" height="7" fill="none" stroke="#ddd"/><path d="M0.5 0.5l4.5 4 4.5-4" fill="none" stroke="#ddd"/></svg>
        ourcustomers@kelvordatawise.com
      </div>
    </div>
    <div class="foot-sep" style="left:357px"></div>

    <h4 class="foot-head" style="left:388px">Follow Us</h4>
    <ul class="social-list">
      <li><span class="social-dot"></span>Socialbook</li>
      <li><span class="social-dot"></span>Careerlink</li>
      <li><span class="social-dot"></span>Chirpline</li>
    </ul>
    <div class="foot-sep" style="left:477px"></div>

    <div class="foot-logo"><span class="logo-mark"></span><span class="logo-name">Kelvor Datawise Solutions</span></div>

    <div class="foot-rule"></div>
    <p class="copyright">COPYRIGHT © 2016 KELVOR DATAWISE SOLUTIONS. ALL RIGHTS RESERVED.</p>
  </footer>

</main>
</body>
</html>
```